Surgical Conditions of the thyroid and parathyroid glands - a flyer for GPs

Hi there,

I am a thyroid surgeon trying to produce a bi-fold A4 flyer as a quick reference guide for general practitioners (family doctors). It needs to feel friendly and professional.

The text for the four "pages" can be found in the "thyroid flyer for design" document attached.

The front page should have:
- The title
- the photo with the patient having an ultrasound
- the photo of the asian woman with the enlarged thyroid gland
- possibly the photo of the blonde woman touching her neck

The inner two pages are predominantly text - I would love this to be presented in an easy to read, uncluttered format. There is a photo attached which demonstrates the parathyroid glands. This should be placed near the parathyroid text section if possible.

The back page is a brief bio of myself. It should have the profile pic attached.
It should have contact details, which I forgot to put in the word document. These details are:
Phone (03) 9418 2759 for all appointments
Consulting at:
27 Pellory Lane, Berwick, VIC 3806
norvalesurgical.example.au
tobinmarwick.example

The back page should also have the "Tarrow Health" and "Guild of Operatives" logos.

If possible, all pages should have the "Norvale Surgical Group" logo.

The whole feel could have a similar colour scheme to my group website (largely orange and green). Please see www.norvalesurgical.example.au for examples.

Many thanks!

Target Market(s)

General practitioners (ie family doctors)

Industry/Entity Type

Medical And Science

Font styles to use
Sans Serif

Colors
33b8a4
f78f20

Requirements
Must have
• Contact details on the back, norvale surgical group logo on front and back pages, Tarrow Health and Guild of Operatives logo on the back.
Nice to have
• Other medical/surgical related images as you see fit - sorry to be so broad!!

```html
<!DOCTYPE html>
<html lang="en">
<head>
<meta charset="utf-8">
<title>Thyroid and Parathyroid Quick Reference – Norvale Surgical Group</title>
<link href="https://fonts.googleapis.com/css2?family=Encode+Sans:ital,wght@0,400;0,500;0,600;0,700;1,400;1,500&display=swap" rel="stylesheet">
<style>
  :root {
    --teal: #33b8a4;
    --teal-dark: #2aa593;
    --orange: #f78f20;
    --peach: #fde4cd;
    --ink: #231f20;
    --paper: #ffffff;
    --logo-grey: #4d4d4f;
  }
  * { box-sizing: border-box; margin: 0; padding: 0; }
  html, body { width: 1200px; height: 849px; overflow: hidden; background: var(--paper); }
  body {
    position: relative;
    font-family: "Encode Sans", Arial, sans-serif;
    color: var(--ink);
    font-size: 13px;
    line-height: 1.32;
  }
  .panel { position: absolute; border: 1.5px solid var(--teal); background: var(--paper); }
  .panel--orange { border-color: var(--orange); }
  .panel__title {
    height: 35px;
    background: var(--teal);
    color: #fff;
    font-weight: 600;
    font-size: 17.5px;
    padding: 6px 8px;
    letter-spacing: 0.1px;
  }
  .panel--orange .panel__title { background: var(--orange); }
  .panel__body { padding: 10px 8px; }

  /* Common thyroid disorders */
  .disorders { left: 18px; top: 24px; width: 566px; height: 299px; }
  .disorders p { margin-bottom: 12px; }
  .term { color: var(--teal); font-weight: 600; }

  /* Symptoms */
  .symptoms { left: 18px; top: 338px; width: 566px; height: 255px; }
  .symptoms .panel__body { display: flex; padding: 3px 8px; }
  .symptom-col { width: 287px; }
  .symptom-col h3 { color: var(--teal); font-weight: 600; font-size: 15px; line-height: 1.2; margin-bottom: 1px; }
  .symptom-col ul { list-style: none; line-height: 1.31; }
  .symptom-col h3.gap { margin-top: 18px; }

  /* Workup */
  .workup { left: 18px; top: 610px; width: 566px; height: 218px; }
  .workup .panel__body { padding: 10px 10px; }
  .workup p { text-align: justify; margin-bottom: 6px; }
  .workup em { font-style: italic; font-weight: 500; }

  /* FNA */
  .fna { left: 615px; top: 24px; width: 566px; height: 300px; }
  .fna .photo { position: absolute; left: 5px; top: 44px; width: 124px; height: 124px; border-radius: 50%;
    background: radial-gradient(circle at 45% 40%, #e8b8a0 0%, #c8403a 55%, #8e1f1f 100%); border: 3px solid var(--orange); }
  .fna ul { list-style: none; }
  .fna .bullet { position: relative; padding-left: 16px; }
  .fna .bullet::before { content: "•"; position: absolute; left: 0; }
  .fna .sub { padding-left: 14px; text-indent: -8px; }
  .fna .upper { position: absolute; left: 137px; top: 43px; width: 420px; }
  .fna .lower { position: absolute; left: 12px; top: 176px; width: 550px; }
  .fna .upper > li { margin-bottom: 0; }

  /* Parathyroid */
  .parathyroid { left: 615px; top: 339px; width: 566px; height: 282px; background: var(--peach); }
  .parathyroid p { position: absolute; text-align: justify; }
  .parathyroid .screening { left: 10px; top: 80px; width: 222px; }
  .parathyroid .testing { left: 10px; top: 190px; width: 262px; }
  .scan-photo { position: absolute; left: 241px; top: 38px; width: 140px; height: 140px; border-radius: 50%;
    background: radial-gradient(circle at 55% 55%, #d9a48e 0%, #9aa7b3 50%, #3d4a5c 100%); border: 3px solid var(--orange); }
  .gland-illustration { position: absolute; left: 332px; top: 22px; width: 240px; height: 250px; border-radius: 50%;
    background: radial-gradient(circle at 50% 50%, #f3f3f3 0%, #d8d8d8 60%, #bdbdbd 100%); border: 3px solid var(--orange); }

  /* Brand */
  .brand { position: absolute; left: 790px; top: 690px; width: 240px; text-align: center; }
  .brand__mark { display: block; margin: 0 auto 14px; width: 70px; height: 70px; border-radius: 50%; background: var(--teal); }
  .brand__name { font-size: 24px; font-weight: 600; color: var(--logo-grey); letter-spacing: 0.5px; }
</style>
</head>
<body>

<section class="panel disorders">
  <h2 class="panel__title">Common thyroid disorders</h2>
  <div class="panel__body">
    <p><span class="term">Solitary nodules</span> – often require characterisation with ultrasound +/- fine needle aspirate to determine likelihood of malignancy</p>
    <p><span class="term">Multinodular goitre</span> – usually benign but may cause compressive symptoms</p>
    <p><span class="term">Graves’ disease</span> – autoimmune stimulation of TSH receptors leading to hyperthyroidism</p>
    <p><span class="term">Thyroid cancer</span> – important risk factors include family history and a history of radiation exposure. Readily treatable with surgery, often in conjunction with radioactive iodine</p>
    <p><span class="term">Hashimoto’s thyroiditis</span> – usually self-limiting, can cause hyperthyroidism (early) or hypothyroidism (late). May benefit from surgery if associated with ongoing pain</p>
    <p><span class="term">Thyroglossal cyst</span> – presents as a midline lump above the thyroid cartilage (Adam’s apple), may become inflamed or form fistulas to the overlying skin</p>
  </div>
</section>

<section class="panel symptoms">
  <h2 class="panel__title">Common symptoms of thyroid disease</h2>
  <div class="panel__body">
    <div class="symptom-col">
      <h3>Symptoms of hyperthyroidism</h3>
      <ul><li>Tiredness</li><li>Palpitations</li><li>Tremor</li><li>Sweats</li><li>Heat intolerance</li><li>exophthalmos</li><li>Diarrhoea</li><li>Weight loss</li><li>Menorrhagia</li></ul>
    </div>
    <div class="symptom-col">
      <h3>Symptoms of hypothyroidism</h3>
      <ul><li>Lethargy</li><li>Weight gain</li><li>Weakness</li><li>Cold</li><li>Hair loss</li></ul>
      <h3 class="gap">Compressive symptoms</h3>
      <ul><li>Lump in the neck</li><li>Dysphagia</li><li>Dyspnoea</li><li>Voice change</li></ul>
    </div>
  </div>
</section>

<section class="panel workup">
  <h2 class="panel__title">Workup for thyroid disorders</h2>
  <div class="panel__body">
    <p>Most thyroid disorders requiring surgical intervention can be diagnosed with a <em>thyroid ultrasound</em> and <em>thyroid function tests</em>.</p>
    <p>If a patient is biochemically hyperthyroid, a <em>thyroid nuclear scan and anti-TSH receptor antibodies</em> are useful to determine the underlying cause (eg Graves’ disease, toxic nodule or toxic goitre). <em>Thyroid antibodies</em> can also determine if there is underlying thyroiditis. All patients with thyroid disease should also undergo screening for concurrent parathyroid disease with <em>PTH</em>, <em>calcium</em> and <em>vitamin D</em> levels.</p>
    <p>A nodule with suspicious features on ultrasound (increased vascularity, microcalcifications, irregular border) should <em>undergo ultrasound-guided fine needle aspirate</em>.</p>
  </div>
</section>

<section class="panel panel--orange fna">
  <h2 class="panel__title">Which nodules should undergo fine needle aspirate?</h2>
  <div class="photo" role="img" aria-label="Photo of a fine needle aspirate being taken from a patient's neck"></div>
  <ul class="upper">
    <li class="bullet">Nodules &lt;1 cm
      <div class="sub">- If there are suspicious features on ultrasound (irregular border, microcalcifications, increased vascularity)</div>
      <div class="sub">- Nodules without suspicious features less than 1 cm can be re-evaluated with an ultrasound in 1 year</div>
    </li>
    <li class="bullet" style="margin-top:5px">Nodules 1 to 3 cm
      <div class="sub">- Should undergo FNA, especially if there are suspicious features</div>
    </li>
  </ul>
  <ul class="lower">
    <li class="bullet">Nodules &gt;3cm
      <div class="sub">- Should undergo FNA</div>
      <div class="sub">- These nodules are more likely to become symptomatic and there is an increased risk of a false negative FNA with nodules of this size. They should therefore be considered for excision via a hemithyroidectomy. An FNA can determine if a total thyroidectomy is preferred in the case of malignancy.</div>
    </li>
  </ul>
</section>

<section class="panel panel--orange parathyroid">
  <h2 class="panel__title">Parathyroid disease</h2>
  <div class="gland-illustration" role="img" aria-label="Illustration of the thyroid gland with the four parathyroid glands highlighted in red"></div>
  <div class="scan-photo" role="img" aria-label="Photo of a patient having a neck ultrasound"></div>
  <p class="screening">Simple screening with calcium and PTH levels can detect hyperparathyroidism before symptoms become evident.</p>
  <p class="testing">Patients with osteoporosis, recurrent kidney stones or pathological fractures should be tested, as well as with an ultrasound to look for concurrent thyroid issues.</p>
</section>

<div class="brand">
  <span class="brand__mark"></span>
  <span class="brand__name">Norvale Surgical Group</span>
</div>

</body>
</html>
```